Need Powerpoint masters for my consulting company in privacy (RGPD) and IT

For my newly created consulting company I need powerpoint slides masters.
The company is specialzed in privacy (RGPD) and IT.
The company already has a logo (obtained via Pixelhive).
These master slides will be mainly used when presenting reports/analysis to clients.
I'll attach a PNG files of the logo.

```html
<!DOCTYPE html>
<html lang="en">
<head>
<meta charset="utf-8">
<title>Marceau Conseil — Presentation Masters</title>
<link href="https://fonts.googleapis.com/css2?family=Montserrat:wght@300;400;500;600;700&display=swap" rel="stylesheet">
<style>
:root{
  --navy:#072b45;
  --navy-2:#0b3a57;
  --teal:#0c8a98;
  --teal-dark:#0a6b80;
  --grey:#8a8f94;
  --ink:#3b4650;
  --muted:#8b959d;
  --line:#e3e8ec;
  --paper:#ffffff;
  --canvas:#e5e5e5;
  --faint:#eef4f6;
}
*{box-sizing:border-box}
html,body{margin:0;width:1200px;height:2274px;overflow:hidden;background:var(--canvas);font-family:"Montserrat",sans-serif;color:var(--ink)}
.sheet{display:grid;grid-template-columns:repeat(3,387px);grid-auto-rows:218px;gap:8px;padding:11px}
.slide{position:relative;overflow:hidden;background:var(--paper)}
.abs{position:absolute}
.bg-teal{background:linear-gradient(90deg,#0b5f7a,#0d8d9b)}
.bg-navy{background:var(--navy)}
.photo-navy{background:linear-gradient(120deg,#1c4257 0%,#0b2b42 55%,#173f55 100%)}
.photo-teal{background:linear-gradient(120deg,#3a8f93 0%,#0f7486 50%,#0a5d74 100%)}
.photo-city{background:linear-gradient(180deg,#2f7f8c 0%,#136a7c 55%,#0b4f66 100%)}
.photo-street{background:linear-gradient(150deg,#dfe6ea 0%,#b79c6c 45%,#3c4a56 100%)}
.photo-peak{background:linear-gradient(180deg,#8a9ba5 0%,#4d5e68 55%,#1e2a31 100%)}
.faint-block{position:absolute;border-radius:14px;background:rgba(255,255,255,.12)}
.faint-block.light{background:var(--faint)}
.brand{position:absolute;display:flex;flex-direction:column;align-items:flex-start;gap:3px;font-size:7px;font-weight:500;color:#fff;letter-spacing:.2px}
.brand.center{align-items:center}
.brand.row{flex-direction:row;align-items:center;gap:4px}
.brand-mark{width:10px;height:10px;border:1.6px solid currentColor;border-radius:2px}
.brand.navy{color:var(--navy)}
.cover-title{position:absolute;font-weight:700;color:#fff;font-size:20px;line-height:1.3;letter-spacing:.3px}
.cover-meta{position:absolute;font-size:6px;color:#e6f2f4;line-height:1.35}
.footer{position:absolute;left:0;right:0;bottom:0;height:36px;background:#fff}
.presenter{position:absolute;right:20px;top:14px;font-size:6px;font-weight:700;color:var(--navy)}
.big-title{position:absolute;left:0;right:0;text-align:center;font-size:23px;font-weight:600;line-height:1;color:#fff}
.big-sub{position:absolute;left:0;right:0;text-align:center;font-size:9px;color:#fff}
.pill{position:absolute;height:13px;border-radius:8px;font-size:5.5px;letter-spacing:1.2px;display:flex;align-items:center;justify-content:center;color:#fff}
.pill.glass{background:rgba(255,255,255,.18)}
.pill.teal{background:var(--teal)}
.pill.navy{background:var(--navy)}
.pill.date{font-size:7px;font-weight:700;letter-spacing:0;height:16px}
.break-title{position:absolute;left:46px;top:72px;font-size:31px;font-weight:300;color:#fff;line-height:.95}
.break-text{position:absolute;left:46px;top:148px;width:160px;font-size:5.2px;color:#d8ecef;line-height:1.35}
/* content slides */
.rail{position:absolute;left:20px;top:0;bottom:0;width:1px;background:var(--line)}
.rail-mark{position:absolute;left:6px;top:8px;width:10px;height:8px;border:1.6px solid var(--navy);border-radius:2px}
.rail-label{position:absolute;left:5px;top:112px;transform:rotate(-90deg);transform-origin:left top;font-size:3.6px;letter-spacing:.8px;color:#a9b2b9;white-space:nowrap;font-weight:600}
.page-no{position:absolute;left:8px;bottom:6px;font-size:4px;color:var(--muted)}
.s-title{position:absolute;font-size:16px;font-weight:600;color:var(--navy)}
.s-title.center{left:0;right:0;text-align:center}
.bar{position:absolute;width:17px;height:3px;background:var(--teal)}
.body{position:absolute;font-size:5px;line-height:1.4;color:#555f68}
.body p{margin:0 0 5px}
.label{font-size:6px;font-weight:700;color:var(--navy)}
.tiny{font-size:4.4px;line-height:1.35;color:#6b7680}
.col-box{position:absolute;top:92px;width:88px;height:78px;border-radius:3px;color:#fff;text-align:center;padding:28px 8px 0}
.col-box .label{color:#fff;font-size:5px}
.col-box .tiny{color:#e6f0f2}
.col-icon{position:absolute;top:-14px;left:30px;width:28px;height:28px;border-radius:50%;background:#fff;border:2px solid #dce3e7}
.icon-row{position:absolute;display:flex;gap:10px;width:160px}
.icon-sq{flex:none;width:12px;height:13px;border:1px solid var(--navy);border-radius:2px}
.icon-row .label{color:var(--teal);font-size:4.6px}
table.chart{position:absolute;left:30px;top:52px;border-collapse:separate;border-spacing:0 2.4px;font-size:4.4px}
table.chart th{background:var(--navy);color:#fff;height:14px;width:59px;font-weight:600}
table.chart th.blank{background:none}
table.chart td{height:14px;text-align:center;color:#8a939a;border-bottom:1px solid var(--line)}
table.chart td.row-label{background:var(--navy);color:#fff;width:95px;font-weight:600;border:0}
.ok{color:var(--teal);font-weight:700;font-size:7px}
.no{color:var(--navy);font-weight:700;font-size:7px}
.quote-mark{font-size:26px;font-weight:700;color:var(--teal);line-height:1}
.avatar{width:18px;height:18px;border-radius:50%;background:#e6ebee;display:inline-block;vertical-align:middle}
.check{width:12px;height:12px;background:var(--navy);border-radius:1px;display:inline-block}
.step-name{position:absolute;top:142px;width:66px;text-align:center}
.gantt-row{position:absolute;left:40px;font-size:3.8px;color:var(--navy);font-weight:600}
.gantt-bar{position:absolute;height:5px;border-radius:3px;background:var(--navy)}
.contact{position:absolute;left:52px;width:104px;height:26px;background:#fff;box-shadow:0 1px 5px rgba(0,0,0,.1);display:flex;align-items:center;gap:8px;padding-left:12px;font-size:4.2px;color:#6b7680}
.contact.lead{background:var(--teal);color:#fff}
.dot-icon{width:8px;height:8px;border-radius:50%;border:1.4px solid var(--navy)}
.contact.lead .dot-icon{border-color:#fff}
</style>
</head>
<body>
<main class="sheet">

<!-- 1 -->
<section class="slide bg-teal">
  <div class="faint-block" style="left:205px;top:30px;width:170px;height:170px"></div>
  <div class="brand" style="left:28px;top:48px"><span class="brand-mark"></span><span>Marceau Conseil</span></div>
  <h1 class="cover-title" style="left:24px;top:82px;margin:0">TITLE OF<br>PRESENTATION</h1>
  <div class="cover-meta" style="left:26px;top:152px">Here is A place for Credentials<br>Date: 2021 March</div>
</section>

<!-- 2 -->
<section class="slide bg-teal">
  <div class="abs photo-navy" role="img" aria-label="Photo of a consultant in a suit" style="left:203px;top:28px;width:172px;height:170px;border-radius:14px"></div>
  <div class="brand" style="left:28px;top:48px"><span class="brand-mark"></span><span>Marceau Conseil</span></div>
  <h1 class="cover-title" style="left:24px;top:82px;margin:0">TITLE OF<br>PRESENTATION</h1>
  <div class="cover-meta" style="left:26px;top:152px">Here is A place for Credentials<br>Date: 2021 March</div>
</section>

<!-- 3 -->
<section class="slide">
  <div class="abs bg-teal" style="left:0;top:0;width:387px;height:182px"></div>
  <div class="faint-block" style="left:222px;top:12px;width:150px;height:150px"></div>
  <h1 class="cover-title" style="left:20px;top:68px;margin:0">TITLE OF<br>PRESENTATION</h1>
  <div class="cover-meta" style="left:22px;top:138px">Here is A place for Credentials<br>Date: 2021 March</div>
  <div class="footer"><div class="brand navy" style="left:18px;top:8px"><span class="brand-mark"></span><span>Marceau Conseil</span></div><span class="presenter">Presenter Name</span></div>
</section>

<!-- 4 -->
<section class="slide">
  <div class="abs photo-navy" role="img" aria-label="Photo of a consultant holding a tablet" style="left:0;top:0;width:387px;height:182px"></div>
  <div class="abs photo-teal" role="img" aria-label="Photo of a business handshake" style="left:200px;top:14px;width:150px;height:160px;border-radius:12px;opacity:.85"></div>
  <h1 class="cover-title" style="left:20px;top:68px;margin:0">TITLE OF<br>PRESENTATION</h1>
  <div class="cover-meta" style="left:22px;top:138px">Here is A place for Credentials<br>Date: 2021 March</div>
  <div class="footer"><div class="brand navy" style="left:18px;top:8px"><span class="brand-mark"></span><span>Marceau Conseil</span></div><span class="presenter">Presenter Name</span></div>
</section>

<!-- 5 -->
<section class="slide">
  <div class="abs photo-teal" role="img" aria-label="Photo of a consultant holding a tablet" style="left:0;top:0;width:387px;height:182px"></div>
  <div class="abs photo-navy" role="img" aria-label="Photo of a business handshake" style="left:200px;top:14px;width:150px;height:160px;border-radius:12px;opacity:.8"></div>
  <h1 class="cover-title" style="left:20px;top:68px;margin:0">TITLE OF<br>PRESENTATION</h1>
  <div class="cover-meta" style="left:22px;top:138px">Here is A place for Credentials<br>Date: 2021 March</div>
  <div class="footer"><div class="brand navy" style="left:18px;top:8px"><span class="brand-mark"></span><span>Marceau Conseil</span></div><span class="presenter">Presenter Name</span></div>
</section>

<!-- 6 -->
<section class="slide">
  <div class="faint-block light" style="left:228px;top:28px;width:148px;height:160px"></div>
  <div class="brand navy" style="left:26px;top:36px"><span class="brand-mark"></span><span>Marceau Conseil</span></div>
  <h1 class="abs" style="left:24px;top:80px;margin:0;font-size:23px;font-weight:600;line-height:1;color:var(--navy)">Presentation<br>Title Goes Here</h1>
  <div class="abs" style="left:24px;top:130px;font-size:8px;color:var(--teal)">Sub Title Goes Here</div>
  <div class="pill teal" style="left:20px;top:172px;width:118px">www.websitename.com</div>
</section>

<!-- 7 -->
<section class="slide photo-navy" role="img" aria-label="Photo of a consultant with a tablet, dark blue tint">
  <div class="brand" style="left:28px;top:48px"><span class="brand-mark"></span><span>Marceau Conseil</span></div>
  <h1 class="cover-title" style="left:24px;top:82px;margin:0">TITLE OF<br>PRESENTATION</h1>
  <div class="cover-meta" style="left:26px;top:152px">Here is A place for Credentials<br>Date: 2021 March</div>
</section>

<!-- 8 -->
<section class="slide photo-teal" role="img" aria-label="Photo of a consultant with a tablet, teal tint">
  <div class="brand" style="left:28px;top:48px"><span class="brand-mark"></span><span>Marceau Conseil</span></div>
  <h1 class="cover-title" style="left:24px;top:82px;margin:0">TITLE OF<br>PRESENTATION</h1>
  <div class="cover-meta" style="left:26px;top:152px">Here is A place for Credentials<br>Date: 2021 March</div>
</section>

<!-- 9 -->
<section class="slide">
  <div class="abs photo-teal" role="img" aria-label="Photo of a consultant with a tablet, teal tint" style="left:0;top:0;width:387px;height:182px"></div>
  <div class="pill glass" style="left:118px;top:38px;width:150px">www.websitename.com</div>
  <h1 class="big-title" style="top:70px;margin:0">Presentation<br>Title Goes Here</h1>
  <div class="big-sub" style="top:122px">Sub Title Goes Here</div>
  <div class="pill navy date" style="left:266px;top:168px;width:98px">Oct 2021</div>
  <div class="footer"><div class="brand navy" style="left:14px;top:8px"><span class="brand-mark"></span><span>Marceau Conseil</span></div></div>
</section>

<!-- 10 -->
<section class="slide">
  <div class="abs photo-navy" role="img" aria-label="Photo of a consultant with a tablet, dark blue tint" style="left:0;top:0;width:387px;height:182px"></div>
  <div class="pill glass" style="left:118px;top:38px;width:150px">www.websitename.com</div>
  <h1 class="big-title" style="top:70px;margin:0">Presentation<br>Title Goes Here</h1>
  <div class="big-sub" style="top:122px">Sub Title Goes Here</div>
  <div class="pill teal date" style="left:266px;top:168px;width:98px">Oct 2021</div>
  <div class="footer"><div class="brand navy" style="left:14px;top:8px"><span class="brand-mark"></span><span>Marceau Conseil</span></div></div>
</section>

<!-- 11 -->
<section class="slide photo-navy" role="img" aria-label="Photo of a consultant with a tablet, dark blue tint">
  <div class="brand center" style="left:0;right:0;top:28px"><span class="brand-mark"></span><span>Marceau Conseil</span></div>
  <div class="pill glass" style="left:118px;top:64px;width:150px">www.websitename.com</div>
  <h1 class="big-title" style="top:88px;margin:0">Presentation<br>Title Goes Here</h1>
  <div class="big-sub" style="top:140px">Sub Title Goes Here</div>
  <div class="pill teal" style="left:146px;top:175px;width:84px;height:12px;font-size:5px;letter-spacing:0;font-weight:700">Oct 2021</div>
</section>

<!-- 12 -->
<section class="slide photo-city" role="img" aria-label="Photo of a city skyline, teal tint">
  <div class="brand center" style="left:0;right:0;top:40px"><span class="brand-mark"></span><span>Marceau Conseil</span></div>
  <h1 class="big-title" style="top:82px;margin:0">Presentation<br>Title Goes Here</h1>
  <div class="big-sub" style="top:134px">Sub Title Goes Here</div>
  <div class="pill glass" style="left:118px;top:168px;width:150px">www.websitename.com</div>
</section>

<!-- 13 -->
<section class="slide" style="background:var(--teal)">
  <div class="faint-block" style="left:205px;top:30px;width:170px;height:170px"></div>
  <div class="brand" style="left:46px;top:48px;font-size:5px"><span class="brand-mark" style="width:8px;height:8px"></span><span>Marceau Conseil</span></div>
  <h2 class="break-title" style="margin:0">Slide<br>Break</h2>
  <p class="break-text" style="margin:0">Lorem ipsum dolor sit amet, consectetur adipiscing elit, sed do eiusmod tempor incididunt ut labore et dolore magna aliqua. Lorem ipsum dolor sit amet, consectetur adipiscing elit, sed do eiusmod tempor incididunt ut labore et dolore magna aliqua.</p>
</section>

<!-- 14 -->
<section class="slide bg-navy">
  <div class="faint-block" style="left:205px;top:30px;width:170px;height:170px"></div>
  <div class="brand" style="left:46px;top:48px;font-size:5px"><span class="brand-mark" style="width:8px;height:8px"></span><span>Marceau Conseil</span></div>
  <h2 class="break-title" style="margin:0">Slide<br>Break</h2>
  <p class="break-text" style="margin:0">Lorem ipsum dolor sit amet, consectetur adipiscing elit, sed do eiusmod tempor incididunt ut labore et dolore magna aliqua. Lorem ipsum dolor sit amet, consectetur adipiscing elit, sed do eiusmod tempor incididunt ut labore et dolore magna aliqua.</p>
</section>

<!-- 15 -->
<section class="slide">
  <div class="rail"></div><div class="rail-mark"></div><div class="rail-label">MARCEAU CONSEIL</div><div class="page-no">16</div>
  <div class="faint-block light" style="left:228px;top:30px;width:148px;height:160px"></div>
  <h2 class="s-title" style="left:34px;top:20px;margin:0">Title And Body Slide</h2>
  <div class="bar" style="left:35px;top:46px"></div>
</section>

<!-- 16 -->
<section class="slide">
  <div class="rail"></div><div class="rail-mark"></div><div class="rail-label">MARCEAU CONSEIL</div><div class="page-no">17</div>
  <h2 class="s-title" style="left:34px;top:20px;margin:0">Title And Body Slide</h2>
  <div class="bar" style="left:35px;top:46px"></div>
  <div class="body" style="left:38px;top:62px;width:335px">
    <p>Lorem ipsum dolor sit amet, consectetur adipiscing elit, sed do eiusmod tempor incididunt ut labore et dolore magna aliqua. Ut enim ad minim veniam, quis nostrud exercitation ullamco laboris nisi ut aliquip ex ea commodo consequat.</p>
    <p>Lorem ipsum dolor sit amet, consectetur adipiscing elit, sed do eiusmod tempor incididunt ut labore et dolore magna aliqua. Lorem ipsum dolor sit amet, consectetur adipiscing elit, sed do eiusmod tempor incididunt ut labore. Ut enim ad minim veniam, quis nostrud exercitation.</p>
    <p>Lorem ipsum dolor sit amet, consectetur adipiscing elit, sed do eiusmod tempor incididunt ut labore et dolore magna aliqua. Lorem ipsum dolor sit amet, consectetur adipiscing elit, sed do eiusmod tempor incididunt ut labore et dolore magna aliqua. Sed do eiusmod tempor incididunt ut labore et dolore magna aliqua, consectetur adipiscing elit, quis nostrud exercitation ullamco laboris nisi ut aliquip.</p>
  </div>
</section>

<!-- 17 -->
<section class="slide">
  <div class="rail"></div><div class="rail-mark"></div><div class="rail-label">MARCEAU CONSEIL</div><div class="page-no">17</div>
  <div class="abs bg-navy" style="left:196px;top:48px;width:191px;height:115px"></div>
  <div class="abs photo-street" role="img" aria-label="Photo of a city street at sunset" style="left:218px;top:28px;width:169px;height:125px"></div>
  <h2 class="s-title" style="left:38px;top:66px;margin:0;font-size:19px">Pic And Text</h2>
  <div class="bar" style="left:39px;top:94px"></div>
  <p class="body" style="left:38px;top:104px;width:132px;font-size:5.6px;margin:0;text-align:justify">Lorem ipsum dolor sit amet, consectetur adipiscing elit, sed do eiusmod tempor incididunt ut labore et dolore magna aliqua. Lorem ipsum dolor sit amet, consectetur adipiscing elit, sed do eiusmod tempor incididunt ut labore et dolore magna aliqua. Ut enim ad minim veniam, quis nostrud exercitation ullamco laboris nisi ut aliquip.</p>
</section>

<!-- 18 -->
<section class="slide">
  <div class="abs photo-peak" role="img" aria-label="Photo of a hiker standing on a mountain peak" style="left:0;top:0;width:168px;height:218px"></div>
  <div class="abs" style="left:190px;top:60px;width:40px;height:2px;background:var(--teal)"></div>
  <p class="abs" style="left:190px;top:64px;width:170px;margin:0;font-size:8.4px;font-weight:700;color:var(--navy);line-height:1.3">Success is not only what you achieve in your life, but also what you inspire in the lives of others</p>
  <div class="abs bg-navy" style="left:86px;top:142px;width:301px;height:76px;border-top-left-radius:12px;display:flex;gap:14px;padding:22px 10px 0 24px;color:#fff">
    <div style="width:80px"><div style="font-size:5.2px;font-weight:700">Lorem ipsum dolor</div><div class="tiny" style="color:#c9d6de;margin-top:6px">Lorem ipsum dolor sit amet, consectetur adipiscing elit, sed do eiusmod tempor</div></div>
    <div style="width:80px"><div style="font-size:5.2px;font-weight:700">Lorem ipsum dolor</div><div class="tiny" style="color:#c9d6de;margin-top:6px">Lorem ipsum dolor sit amet, consectetur adipiscing elit, sed do eiusmod tempor</div></div>
    <div style="width:80px"><div style="font-size:5.2px;font-weight:700">Lorem ipsum dolor</div><div class="tiny" style="color:#c9d6de;margin-top:6px">Lorem ipsum dolor sit amet, consectetur adipiscing elit, sed do eiusmod tempor</div></div>
  </div>
</section>

<!-- 19 -->
<section class="slide">
  <div class="rail"></div><div class="rail-mark"></div><div class="rail-label">MARCEAU CONSEIL</div><div class="page-no">19</div>
  <div class="abs bg-navy" style="left:20px;top:0;width:367px;height:110px"></div>
  <h2 class="s-title center" style="top:30px;margin:0;color:#fff;font-size:15px;padding-left:20px">Here Add Awesome Text</h2>
  <div class="bar" style="left:205px;top:56px"></div>
  <svg class="abs" style="left:20px;top:82px" width="367" height="46" viewBox="0 0 367 46">
    <g fill="#0c8a98" stroke="#fff" stroke-width="3">
      <circle cx="71" cy="22" r="20"/><circle cx="180" cy="22" r="20"/><circle cx="288" cy="22" r="20"/>
    </g>
    <g fill="none" stroke="#fff" stroke-width="1.3">
      <circle cx="71" cy="22" r="7"/><circle cx="71" cy="22" r="3"/>
      <path d="M173 29l12-14M178 29l7 0M185 15l-2 6"/>
      <path d="M282 28v-6M288 28v-10M294 28v-14"/>
    </g>
  </svg>
  <div class="abs" style="left:40px;top:134px;width:330px;display:flex;justify-content:space-between;text-align:center">
    <div style="width:96px"><div class="label">Project name</div><div class="tiny" style="margin-top:6px">Lorem ipsum dolor sit amet, nec an dictas equidem appellantur, ut has commune accommodare mea illum.</div></div>
    <div style="width:96px"><div class="label">Project name</div><div class="tiny" style="margin-top:6px">Lorem ipsum dolor sit amet, nec an dictas equidem appellantur, ut has commune accommodare mea illum.</div></div>
    <div style="width:96px"><div class="label">Project name</div><div class="tiny" style="margin-top:6px">Lorem ipsum dolor sit amet, nec an dictas equidem appellantur, ut has commune accommodare mea illum.</div></div>
  </div>
</section>

<!-- 20 -->
<section class="slide">
  <div class="rail"></div><div class="rail-mark"></div><div class="rail-label">MARCEAU CONSEIL</div><div class="page-no">20</div>
  <h2 class="s-title center" style="top:18px;margin:0;font-size:15px">3 Columns Slide</h2>
  <div class="bar" style="left:185px;top:42px"></div>
  <div class="col-box" style="left:53px;background:var(--teal)"><span class="col-icon"></span><div class="label">Project name here</div><div class="tiny" style="margin-top:3px">Lorem ipsum dolor sit amet, nec an dictas equidem appellantur, ut has commune accommodare.</div></div>
  <div class="col-box" style="left:152px;background:var(--navy)"><span class="col-icon"></span><div class="label">Project name here</div><div class="tiny" style="margin-top:3px">Lorem ipsum dolor sit amet, nec an dictas equidem appellantur, ut has commune accommodare.</div></div>
  <div class="col-box" style="left:251px;background:var(--grey)"><span class="col-icon"></span><div class="label">Project name here</div><div class="tiny" style="margin-top:3px">Lorem ipsum dolor sit amet, nec an dictas equidem appellantur, ut has commune accommodare.</div></div>
</section>

<!-- 21 -->
<section class="slide">
  <div class="rail"></div><div class="rail-mark"></div><div class="rail-label">MARCEAU CONSEIL</div><div class="page-no">21</div>
  <h2 class="s-title center" style="top:16px;margin:0;font-size:15px">6 Columns Slide</h2>
  <div class="bar" style="left:185px;top:40px"></div>
  <div class="icon-row" style="left:38px;top:64px"><span class="icon-sq"></span><div><div class="label">Project name</div><div class="tiny">Lorem ipsum dolor sit amet, nec an dictas equidem appellantur, ut has commune accommodare.</div></div></div>
  <div class="icon-row" style="left:206px;top:64px"><span class="icon-sq"></span><div><div class="label">Project name</div><div class="tiny">Lorem ipsum dolor sit amet, nec an dictas equidem appellantur, ut has commune accommodare.</div></div></div>
  <div class="icon-row" style="left:38px;top:104px"><span class="icon-sq"></span><div><div class="label">Project name</div><div class="tiny">Lorem ipsum dolor sit amet, nec an dictas equidem appellantur, ut has commune accommodare.</div></div></div>
  <div class="icon-row" style="left:206px;top:104px"><span class="icon-sq"></span><div><div class="label">Project name</div><div class="tiny">Lorem ipsum dolor sit amet, nec an dictas equidem appellantur, ut has commune accommodare.</div></div></div>
  <div class="icon-row" style="left:38px;top:144px"><span class="icon-sq"></span><div><div class="label">Project name</div><div class="tiny">Lorem ipsum dolor sit amet, nec an dictas equidem appellantur, ut has commune accommodare.</div></div></div>
  <div class="icon-row" style="left:206px;top:144px"><span class="icon-sq"></span><div><div class="label">Project name</div><div class="tiny">Lorem ipsum dolor sit amet, nec an dictas equidem appellantur, ut has commune accommodare.</div></div></div>
</section>

<!-- 22 -->
<section class="slide">
  <div class="rail"></div><div class="rail-mark"></div><div class="rail-label">MARCEAU CONSEIL</div><div class="page-no">22</div>
  <h2 class="s-title center" style="top:16px;margin:0;font-size:15px">Chart Slide</h2>
  <table class="chart">
    <tr><th class="blank"></th><th>Your Text Here</th><th>Your Text Here</th><th>Your Text Here</th><th>Your Text Here</th></tr>
    <tr><td class="row-label">You can replace this text</td><td>1250</td><td class="ok">✓</td><td>50%</td><td>1252</td></tr>
    <tr><td class="row-label">You can replace this text</td><td>3623</td><td class="no">✕</td><td>50%</td><td>3623</td></tr>
    <tr><td class="row-label">You can replace this text</td><td>2569</td><td class="ok">✓</td><td>12%</td><td>2569</td></tr>
    <tr><td class="row-label">You can replace this text</td><td>1020</td><td class="no">✕</td><td>85%</td><td>1020</td></tr>
    <tr><td class="row-label">You can replace this text</td><td>2320</td><td class="ok">✓</td><td>36%</td><td>2320</td></tr>
    <tr><td class="row-label">You can replace this text</td><td>5698</td><td class="no">✕</td><td>95%</td><td>5698</td></tr>
    <tr><td class="row-label">You can replace this text</td><td>1999</td><td class="no">✕</td><td>66%</td><td>1999</td></tr>
  </table>
</section>

<!-- 23 -->
<section class="slide">
  <div class="rail"></div><div class="rail-mark"></div><div class="rail-label">MARCEAU CONSEIL</div><div class="page-no">23</div>
  <h2 class="s-title" style="left:34px;top:20px;margin:0">Smart Art Slide</h2>
  <div class="bar" style="left:35px;top:44px"></div>
  <div class="icon-row" style="left:36px;top:72px;width:150px"><span class="avatar" style="width:12px;height:12px;border:1px solid var(--navy);background:none"></span><div><div class="label" style="color:var(--navy)">Lorem ipsum dolor</div><div class="tiny">Lorem ipsum dolor sit amet, consectetur adipiscing elit, sed do eiusmod tempor eta beta.</div></div></div>
  <div class="icon-row" style="left:36px;top:115px;width:150px"><span class="avatar" style="width:12px;height:12px;border:1px solid var(--navy);background:none"></span><div><div class="label" style="color:var(--navy)">Lorem ipsum dolor</div><div class="tiny">Lorem ipsum dolor sit amet, consectetur adipiscing elit, sed do eiusmod tempor eta beta.</div></div></div>
  <div class="icon-row" style="left:36px;top:160px;width:150px"><span class="avatar" style="width:12px;height:12px;border:1px solid var(--navy);background:none"></span><div><div class="label" style="color:var(--navy)">Lorem ipsum dolor</div><div class="tiny">Lorem ipsum dolor sit amet, consectetur adipiscing elit, sed do eiusmod tempor eta beta.</div></div></div>
  <svg class="abs" style="left:200px;top:52px" width="170" height="150" viewBox="0 0 170 150">
    <path d="M85 2 L125 72 L45 72 Z" fill="#0c8a98" stroke-linejoin="round"/>
    <path d="M43 78 L82 78 L82 145 L4 145 Z" fill="#072b45"/>
    <path d="M88 78 L127 78 L166 145 L88 145 Z" fill="#0a6b80"/>
    <g fill="#fff" font-family="Montserrat,sans-serif" text-anchor="middle">
      <text x="85" y="45" font-size="5" font-weight="700">Project</text><text x="85" y="51" font-size="5" font-weight="700">name</text>
      <text x="85" y="58" font-size="3.4">Lorem ipsum dolor sit</text>
      <text x="56" y="108" font-size="5" font-weight="700">Project name</text><text x="56" y="116" font-size="3.4">Lorem ipsum dolor sit</text>
      <text x="114" y="108" font-size="5" font-weight="700">Project name</text><text x="114" y="116" font-size="3.4">Lorem ipsum dolor sit</text>
    </g>
  </svg>
</section>

<!-- 24 -->
<section class="slide">
  <div class="rail"></div><div class="rail-mark"></div><div class="rail-label">MARCEAU CONSEIL</div><div class="page-no">24</div>
  <h2 class="s-title center" style="top:16px;margin:0;font-size:15px">Here is Quotes</h2>
  <div class="bar" style="left:185px;top:40px"></div>
  <div class="abs" style="left:38px;top:62px;width:145px">
    <div class="quote-mark">”</div>
    <p style="font-size:6px;line-height:1.55;color:#55606a;margin:2px 0 10px">Lorem ipsum dolor sit amet, consectetur adipiscing elit, sed do eiusmod tempor incididunt ut labore et dolore magna aliqua. Lorem ipsum dolor sit amet, consectetur adipiscing elit.</p>
    <span class="avatar"></span> <span style="display:inline-block;vertical-align:middle;font-size:5px"><b style="color:var(--teal)">Your Name</b><br>Founder</span>
  </div>
  <div class="abs" style="left:216px;top:62px;width:145px">
    <div class="quote-mark">”</div>
    <p style="font-size:6px;line-height:1.55;color:#55606a;margin:2px 0 10px">Lorem ipsum dolor sit amet, consectetur adipiscing elit, sed do eiusmod tempor incididunt ut labore et dolore magna aliqua. Lorem ipsum dolor sit amet, consectetur adipiscing elit.</p>
    <span class="avatar"></span> <span style="display:inline-block;vertical-align:middle;font-size:5px"><b style="color:var(--teal)">Your Name</b><br>Founder</span>
  </div>
</section>

<!-- 25 -->
<section class="slide">
  <div class="rail"></div><div class="rail-mark"></div><div class="rail-label">MARCEAU CONSEIL</div><div class="page-no">25</div>
  <h2 class="s-title center" style="top:20px;margin:0;font-size:15px">Here Is Statistics</h2>
  <div class="bar" style="left:185px;top:44px"></div>
  <svg class="abs" style="left:30px;top:60px" width="190" height="140" viewBox="0 0 190 140">
    <circle cx="60" cy="70" r="58" fill="#072b45"/>
    <circle cx="60" cy="84" r="44" fill="#0c8a98"/>
    <circle cx="60" cy="106" r="22" fill="#55585b"/>
    <g stroke="#8b959d" stroke-width=".6"><line x1="60" y1="33" x2="140" y2="33"/><line x1="60" y1="67" x2="140" y2="67"/><line x1="60" y1="108" x2="140" y2="108"/></g>
    <g fill="#fff" font-family="Montserrat,sans-serif" font-size="13" font-weight="700" text-anchor="middle"><text x="60" y="37">$</text><text x="60" y="72">$</text><text x="60" y="111">$</text></g>
    <g fill="#072b45" font-family="Montserrat,sans-serif" font-size="10" font-weight="700"><text x="144" y="37">5M</text><text x="144" y="71">2M</text><text x="144" y="112">1M</text></g>
  </svg>
  <div class="abs" style="left:236px;top:88px;width:140px;display:flex;flex-direction:column;gap:15px">
    <div style="display:flex;gap:8px"><span class="check"></span><div><div class="label">Lorem ipsum dolor</div><div class="tiny">Lorem ipsum dolor sit amet, consectetur adipiscing elit, sed do eiusmod tempor</div></div></div>
    <div style="display:flex;gap:8px"><span class="check" style="background:var(--teal)"></span><div><div class="label">Lorem ipsum dolor</div><div class="tiny">Lorem ipsum dolor sit amet, consectetur adipiscing elit, sed do eiusmod tempor</div></div></div>
    <div style="display:flex;gap:8px"><span class="check" style="background:#55585b"></span><div><div class="label">Lorem ipsum dolor</div><div class="tiny">Lorem ipsum dolor sit amet, consectetur adipiscing elit, sed do eiusmod tempor</div></div></div>
  </div>
</section>

<!-- 26 -->
<section class="slide">
  <div class="rail"></div><div class="rail-mark"></div><div class="rail-label">MARCEAU CONSEIL</div><div class="page-no">26</div>
  <h2 class="s-title center" style="top:20px;margin:0;font-size:15px">Here Add Your Title</h2>
  <div class="bar" style="left:185px;top:44px"></div>
  <p class="abs" style="left:74px;width:240px;top:56px;margin:0;text-align:center;font-size:5.2px;line-height:1.5;color:#6b7680">Lorem Ipsum is the printing and typesetting industry. Lorem Ipsum has been the industry's standard dummy text ever since the 1500s, when an unknown printer took a galley of type and scrambled it to make a type specimen book. It has survived not only five centuries.</p>
  <svg class="abs" style="left:70px;top:102px" width="250" height="80" viewBox="0 0 250 80">
    <g fill="none" stroke-width="4">
      <circle cx="38" cy="30" r="26" stroke="#e3e8ec"/><circle cx="38" cy="30" r="26" stroke="#0c8a98" stroke-dasharray="81.7 163.4" transform="rotate(-90 38 30)"/>
      <circle cx="123" cy="30" r="26" stroke="#e3e8ec"/><circle cx="123" cy="30" r="26" stroke="#072b45" stroke-dasharray="122.5 163.4" transform="rotate(-90 123 30)"/>
      <circle cx="205" cy="30" r="26" stroke="#e3e8ec"/><circle cx="205" cy="30" r="26" stroke="#0c8a98" stroke-dasharray="65.3 163.4" transform="rotate(-90 205 30)"/>
    </g>
    <g fill="#072b45" font-family="Montserrat,sans-serif" font-size="12" font-weight="600" text-anchor="middle"><text x="38" y="34">50%</text><text x="123" y="34">75%</text><text x="205" y="34">40%</text></g>
    <g fill="#8b959d" font-family="Montserrat,sans-serif" font-size="4" text-anchor="middle"><text x="38" y="68">Lorem ipsum dolor amet</text><text x="38" y="74">amet consectetur dolor</text><text x="123" y="68">Lorem ipsum dolor amet</text><text x="123" y="74">amet consectetur dolor</text><text x="205" y="68">Lorem ipsum dolor amet</text><text x="205" y="74">amet consectetur dolor</text></g>
  </svg>
</section>

<!-- 27 -->
<section class="slide">
  <div class="rail"></div><div class="rail-mark"></div><div class="rail-label">MARCEAU CONSEIL</div><div class="page-no">27</div>
  <h2 class="s-title center" style="top:16px;margin:0;font-size:15px">Here is Statistics</h2>
  <div class="bar" style="left:185px;top:40px"></div>
  <div class="abs" style="left:28px;top:68px;width:92px;height:56px;background:var(--teal);color:#fff;text-align:center;padding-top:14px"><div style="font-size:15px;font-weight:300">$0.5M</div><div style="font-size:4.4px">Revenue</div></div>
  <div class="abs" style="left:28px;top:124px;width:92px;height:56px;background:#fff;box-shadow:0 1px 5px rgba(0,0,0,.1);color:var(--teal);text-align:center;padding-top:14px"><div style="font-size:14px;font-weight:300">-0.28%</div><div style="font-size:4.4px">Revenue</div></div>
  <svg class="abs" style="left:140px;top:64px" width="240" height="130" viewBox="0 0 240 130">
    <g fill="#8b959d" font-family="Montserrat,sans-serif" font-size="3.8" text-anchor="end">
      <text x="22" y="6">$350,000</text><text x="22" y="21">$300,000</text><text x="22" y="36">$250,000</text><text x="22" y="51">$200,000</text><text x="22" y="66">$150,000</text><text x="22" y="81">$100,000</text><text x="22" y="96">$50,000</text><text x="22" y="111">$-</text>
    </g>
    <g fill="#8b959d" font-family="Montserrat,sans-serif" font-size="3.8" text-anchor="middle">
      <text x="30" y="122">Jan</text><text x="46" y="122">Feb</text><text x="62" y="122">Mar</text><text x="78" y="122">Apr</text><text x="94" y="122">May</text><text x="110" y="122">Jun</text><text x="126" y="122">Jul</text><text x="142" y="122">Aug</text><text x="158" y="122">Sep</text><text x="174" y="122">Oct</text><text x="190" y="122">Nov</text><text x="206" y="122">Dec</text><text x="222" y="122">Jan</text>
    </g>
    <path d="M30 104 C46 100 58 96 66 94 C76 90 84 68 94 64 C104 60 108 80 118 72 C128 62 134 58 142 64 C152 72 160 80 170 74 C180 66 182 40 192 46 C200 52 204 70 212 54 C218 40 222 26 228 18" fill="none" stroke="#0c8a98" stroke-width="1.4"/>
  </svg>
</section>

<!-- 28 -->
<section class="slide">
  <div class="rail"></div><div class="rail-mark"></div><div class="rail-label">MARCEAU CONSEIL</div><div class="page-no">28</div>
  <h2 class="s-title center" style="top:16px;margin:0;font-size:15px">Company Timeline</h2>
  <div class="bar" style="left:185px;top:40px"></div>
  <svg class="abs" style="left:34px;top:72px" width="340" height="70" viewBox="0 0 340 70">
    <g fill="#0c8a98">
      <path d="M0 0 H54 L64 16 L54 32 H0 L10 16 Z"/>
      <path d="M61 0 H115 L125 16 L115 32 H61 L71 16 Z"/>
      <path d="M122 0 H176 L186 16 L176 32 H122 L132 16 Z"/>
      <path d="M183 0 H237 L247 16 L237 32 H183 L193 16 Z"/>
      <path d="M244 0 H306 L316 16 L306 32 H244 L254 16 Z"/>
    </g>
    <g fill="#fff" font-family="Montserrat,sans-serif" font-size="8.4" font-weight="700" text-anchor="middle"><text x="34" y="19">STEP 01</text><text x="95" y="19">STEP 02</text><text x="156" y="19">STEP 03</text><text x="217" y="19">STEP 04</text><text x="282" y="19">STEP 05</text></g>
    <line x1="0" y1="46" x2="316" y2="46" stroke="#c9d1d7" stroke-width=".7"/>
    <g stroke="#c9d1d7" stroke-width=".7"><line x1="34" y1="40" x2="34" y2="56"/><line x1="95" y1="40" x2="95" y2="56"/><line x1="156" y1="40" x2="156" y2="56"/><line x1="217" y1="40" x2="217" y2="56"/><line x1="282" y1="40" x2="282" y2="56"/></g>
  </svg>
  <div class="step-name" style="left:35px"><div class="label">Project name</div><div class="tiny">Lorem Ipsum is simply dummy text, printer took a galley of type</div></div>
  <div class="step-name" style="left:96px"><div class="label">Project name</div><div class="tiny">Lorem Ipsum is simply dummy text, printer took a galley of type</div></div>
  <div class="step-name" style="left:157px"><div class="label">Project name</div><div class="tiny">Lorem Ipsum is simply dummy text, printer took a galley of type</div></div>
  <div class="step-name" style="left:218px"><div class="label">Project name</div><div class="tiny">Lorem Ipsum is simply dummy text, printer took a galley of type</div></div>
  <div class="step-name" style="left:283px"><div class="label">Project name</div><div class="tiny">Lorem Ipsum is simply dummy text, printer took a galley of type</div></div>
</section>

<!-- 29 -->
<section class="slide">
  <div class="rail"></div><div class="rail-mark"></div><div class="rail-label">MARCEAU CONSEIL</div><div class="page-no">29</div>
  <h2 class="s-title center" style="top:18px;margin:0;font-size:15px">Timeline</h2>
  <div class="bar" style="left:185px;top:42px"></div>
  <svg class="abs" style="left:94px;top:74px" width="278" height="130" viewBox="0 0 278 130">
    <rect width="278" height="10" fill="#0c8a98"/>
    <g fill="#fff" font-family="Montserrat,sans-serif" font-size="4" text-anchor="middle">
      <text x="10" y="7">S</text><text x="31" y="7">M</text><text x="52" y="7">T</text><text x="73" y="7">W</text><text x="94" y="7">T</text><text x="115" y="7">F</text><text x="136" y="7">S</text><text x="157" y="7">S</text><text x="178" y="7">M</text><text x="199" y="7">T</text><text x="220" y="7">W</text><text x="241" y="7">T</text><text x="262" y="7">F</text>
    </g>
    <g stroke="#e3e8ec" stroke-width=".6"><line x1="21" y1="10" x2="21" y2="130"/><line x1="42" y1="10" x2="42" y2="130"/><line x1="63" y1="10" x2="63" y2="130"/><line x1="84" y1="10" x2="84" y2="130"/><line x1="105" y1="10" x2="105" y2="130"/><line x1="126" y1="10" x2="126" y2="130"/><line x1="147" y1="10" x2="147" y2="130"/><line x1="168" y1="10" x2="168" y2="130"/><line x1="189" y1="10" x2="189" y2="130"/><line x1="210" y1="10" x2="210" y2="130"/><line x1="231" y1="10" x2="231" y2="130"/><line x1="252" y1="10" x2="252" y2="130"/></g>
    <g fill="#072b45">
      <rect x="0" y="16" width="84" height="5" rx="2.5"/>
      <rect x="66" y="29" width="70" height="5" rx="2.5"/><rect x="150" y="29" width="58" height="5" rx="2.5"/>
      <rect x="66" y="42" width="80" height="5" rx="2.5"/>
      <rect x="48" y="55" width="120" height="5" rx="2.5"/>
      <rect x="108" y="68" width="104" height="5" rx="2.5"/>
      <rect x="90" y="81" width="146" height="5" rx="2.5"/>
      <rect x="24" y="94" width="38" height="5" rx="2.5"/>
      <rect x="236" y="107" width="38" height="5" rx="2.5"/>
    </g>
  </svg>
  <div class="gantt-row" style="top:89px">First Task</div>
  <div class="gantt-row" style="top:102px">Second Task</div>
  <div class="gantt-row" style="top:115px">Third Task</div>
  <div class="gantt-row" style="top:128px">Fourth Task</div>
  <div class="gantt-row" style="top:141px">Fifth Task</div>
  <div class="gantt-row" style="top:154px">Sixth Task</div>
  <div class="gantt-row" style="top:167px">Seventh Task</div>
  <div class="gantt-row" style="top:180px">Eighth Task</div>
</section>

<!-- 30 -->
<section class="slide" style="background:#f4f6f7">
  <div class="contact lead" style="top:38px"><span class="dot-icon"></span>www.website.com</div>
  <div class="contact" style="top:66px"><svg width="8" height="10" viewBox="0 0 8 10"><path d="M4 9.5C1.5 6 1 5 1 3.8A3 3 0 0 1 7 3.8C7 5 6.5 6 4 9.5Z" fill="none" stroke="#072b45"/></svg>Here to write your company adress</div>
  <div class="contact" style="top:94px"><svg width="8" height="8" viewBox="0 0 8 8"><path d="M1.5 1 L3 1 L3.6 2.8 L2.7 3.5 Q3.6 5 4.6 5.4 L5.3 4.5 L7 5.1 L7 6.6 Q3.5 7 1.2 3.2 Z" fill="#072b45"/></svg>(555) 010-0199</div>
  <div class="contact" style="top:122px"><svg width="9" height="7" viewBox="0 0 9 7"><rect x=".5" y=".5" width="8" height="6" fill="none" stroke="#072b45"/><path d="M.5 .5 L4.5 4 L8.5 .5" fill="none" stroke="#072b45"/></svg>info@website.com</div>
  <div class="abs" style="left:78px;top:156px;display:flex;gap:3px"><span style="width:7px;height:7px;background:var(--teal)"></span><span style="width:7px;height:7px;background:var(--teal)"></span><span style="width:7px;height:7px;background:var(--teal)"></span><span style="width:7px;height:7px;background:var(--teal)"></span></div>
  <div class="abs" style="left:212px;top:92px;font-size:23px;font-weight:600;color:var(--teal)">Thank You</div>
</section>

</main>
</body>
</html>
```